Fun family flyer for photographer

Need a flyer to promote our business moving to Brisbane.

Require a family friendly look targetted to mothers, using our logo and existing images from previous shoots.

Would like to see designs that feature the images heavily, but still have text and fonts that set it aside from other flyers.
Updates

I would like to see some unique fonts being used, so far I have only recieved "canned" fonts, some were just straight out Adobe fonts (on a design site? Really?).

Some SUGGESTIONS would include font use similar to the following:
http://www.glyphbarn.net/oldmarquee.font
http://www.glyphbarn.net/giddy-otter.font

Fun fonts, something that grabs attention.
If you're going to plonk one image in the middle of the page and fill it with text in Courier New, consider not submitting.

I would like colourful, attention grabbing backgrounds.

Target Market(s)

Families

Industry/Entity Type

Business

Requirements
Must have
• Two sides to the flyer
Focus on "fun"
Targetted to mothers
Nice to have
• All photos attached, not necessary but nice.
Should not have
• Anything too "corporate"

```html
<!DOCTYPE html>
<html lang="en">
<head>
<meta charset="utf-8">
<title>Brightfield Studio – Family Photography Flyer</title>
<link rel="stylesheet" href="https://fonts.googleapis.com/css2?family=Rye&family=Short+Stack&display=swap">
<style>
  :root {
    --sky: #a9dde6;
    --sky-light: #c4e9ee;
    --sky-deep: #8fcfdb;
    --ink: #1e1e1e;
    --white: #ffffff;
    --green: #7dc242;
    --pink: #e0489b;
    --blue: #2c9ad6;
    --yellow: #f6d21d;
    --orange: #f39a1e;
    --red: #d62a2a;
    --magenta: #d8247e;
  }
  * { box-sizing: border-box; margin: 0; padding: 0; }
  html, body { width: 803px; height: 1200px; overflow: hidden; background: #efefef; }
  .flyer {
    position: relative;
    width: 803px;
    height: 1200px;
    overflow: hidden;
    background: radial-gradient(ellipse at 30% 40%, var(--sky-light), var(--sky) 60%, var(--sky-deep));
    font-family: "Short Stack", "Comic Sans MS", cursive;
    color: var(--ink);
  }
  .header { position: absolute; left: 0; top: 0; width: 803px; height: 226px; }
  .tagline {
    position: absolute; left: 40px; top: 42px; width: 460px;
    text-align: center; font-size: 26px; line-height: 36px;
  }
  .studio-name {
    position: absolute; left: 44px; top: 172px; width: 450px;
    text-align: center; font-family: "Rye", serif; font-size: 44px; line-height: 48px;
    letter-spacing: 1px; white-space: nowrap;
  }
  .brand-mark {
    position: absolute; left: 520px; top: 50px; width: 248px; height: 170px;
    display: flex; align-items: center; gap: 14px;
  }
  .brand-square { width: 34px; height: 34px; background: var(--ink); flex: none; }
  .brand-text { font-size: 30px; line-height: 36px; color: var(--ink); }
  .rainbow-rule {
    position: absolute; left: 0; top: 236px; width: 803px; height: 8px;
    background: linear-gradient(90deg, var(--blue), var(--green), var(--yellow), var(--orange), var(--pink));
  }
  .paint-drips {
    position: absolute; left: 0; top: 250px; width: 470px; height: 30px;
    background: linear-gradient(90deg, var(--green), var(--pink), var(--blue), var(--yellow), var(--orange), var(--red));
    border-radius: 0 0 16px 16px;
  }
  .splash-top {
    position: absolute; left: 560px; top: 250px; width: 243px; height: 110px;
    background: radial-gradient(ellipse at 60% 40%, rgba(224,72,155,.7), rgba(44,154,214,.4) 55%, transparent 75%);
  }
  .splash-side {
    position: absolute; right: 0; top: 380px; width: 30px; height: 520px;
    background: linear-gradient(180deg, var(--yellow), var(--red), var(--pink), var(--blue));
    opacity: .8;
  }
  .splash-left {
    position: absolute; left: 0; top: 660px; width: 30px; height: 380px;
    background: linear-gradient(180deg, var(--red), var(--yellow), var(--blue));
    opacity: .75;
  }
  .splash-bottom {
    position: absolute; left: 0; top: 990px; width: 520px; height: 210px;
    background: radial-gradient(ellipse at 30% 55%, rgba(216,36,126,.75), rgba(44,154,214,.55) 45%, rgba(246,210,29,.35) 65%, transparent 80%);
  }
  .photo-frame {
    position: absolute; width: 364px; height: 316px;
    background: var(--white); padding: 11px;
    box-shadow: 0 3px 8px rgba(0,0,0,.25);
  }
  .photo { width: 100%; height: 100%; }
  .photo-baby { background: linear-gradient(160deg, #6e5b52, #b9c3d6 55%, #3d3f52); }
  .photo-siblings { background: linear-gradient(160deg, #3f6b2e, #c9a58f 50%, #2e2e2e); }
  .photo-women { background: linear-gradient(160deg, #5d8a3a, #e7d8c6 50%, #7a9a4a); }
  .photo-mother-son { background: linear-gradient(160deg, #6a5a3a, #d9b48f 50%, #3a2f24); }
  .frame-1 { left: 34px; top: 348px; }
  .frame-2 { left: 409px; top: 348px; }
  .frame-3 { left: 34px; top: 674px; }
  .frame-4 { left: 409px; top: 674px; }
  .contact {
    position: absolute; left: 340px; top: 1074px; width: 463px; height: 126px;
    background: linear-gradient(90deg, var(--sky-deep), #c7dd6a 35%, #f6d86a 60%, #f3b26a 80%, #c9d6dc);
    clip-path: polygon(34px 0, 100% 0, 100% 100%, 0 100%, 0 34px);
    padding: 20px 26px 0 0; text-align: right;
  }
  .contact-line { font-size: 26px; line-height: 46px; white-space: nowrap; }
</style>
</head>
<body>
<main class="flyer">
  <header class="header">
    <p class="tagline">For Natural and Comfortable<br>family and Pregnancy<br>Photography in choose</p>
    <h1 class="studio-name">BRIGHTFIELD</h1>
    <div class="brand-mark">
      <span class="brand-square"></span>
      <span class="brand-text">Brightfield<br>Studio</span>
    </div>
  </header>
  <div class="rainbow-rule"></div>
  <div class="paint-drips" role="img" aria-label="Rainbow paint drips"></div>
  <div class="splash-top" role="img" aria-label="Colourful paint splatter"></div>
  <div class="splash-side" role="img" aria-label="Colourful paint splatter"></div>
  <div class="splash-left" role="img" aria-label="Colourful paint splatter"></div>
  <div class="splash-bottom" role="img" aria-label="Colourful paint splatter"></div>

  <figure class="photo-frame frame-1"><div class="photo photo-baby" role="img" aria-label="Photo of a baby boy sitting in a white shirt"></div></figure>
  <figure class="photo-frame frame-2"><div class="photo photo-siblings" role="img" aria-label="Photo of a mother with her daughter and son in a garden"></div></figure>
  <figure class="photo-frame frame-3"><div class="photo photo-women" role="img" aria-label="Photo of three women laughing outdoors"></div></figure>
  <figure class="photo-frame frame-4"><div class="photo photo-mother-son" role="img" aria-label="Photo of a mother touching foreheads with her young son"></div></figure>

  <footer class="contact">
    <p class="contact-line">P: 0412555907</p>
    <p class="contact-line">E: hello@brightfield.com.au</p>
  </footer>
</main>
</body>
</html>
```